Business Card Design

I am starting my therapy private practice. I will be an in home therapist, so I go into family's homes instead of using an office to do family/marriage therapy. Therefore, I do not have an office address. I am looking for something in the black, red, gray, and blue color scheme that appeals to both families, couples and teenagers.

Industry/Entity Type

Business

Contact Information for Business Card

Lena Brightwell, MS, MFT Intern
Marriage and Family Therapy
In Home Therapist
617-482-5190
Lena@LenaBrightwell-example.com

```html
<!DOCTYPE html>
<html lang="en">
<head>
<meta charset="utf-8">
<title>Lena Brightwell – Business Card</title>
<link rel="stylesheet" href="https://fonts.googleapis.com/css2?family=Parisienne&family=Dancing+Script:wght@400&family=Crimson+Text&family=Open+Sans:wght@400&display=swap">
<style>
  :root {
    --page-bg: #f4f4f4;
    --card-black: #020202;
    --frame-outer: #111111;
    --frame-silver: #a9a9a9;
    --accent-red: #c8151b;
    --accent-red-dark: #6e0a0d;
    --silver-light: #f2f2f2;
    --silver-mid: #bdbdbd;
    --silver-dark: #8a8a8a;
    --contact-text: #d9d9d9;
    --ghost: #1b1b1b;
  }
  * { margin: 0; padding: 0; box-sizing: border-box; }
  html, body {
    width: 1200px;
    height: 900px;
    overflow: hidden;
    background: var(--page-bg);
  }
  .canvas {
    position: relative;
    width: 1200px;
    height: 900px;
  }
  .business-card {
    position: absolute;
    left: 150px;
    top: 180px;
    width: 900px;
    height: 540px;
    border-radius: 44px;
    background: var(--frame-outer);
    padding: 8px;
  }
  .card-frame {
    width: 100%;
    height: 100%;
    border-radius: 38px;
    background: var(--frame-silver);
    padding: 12px;
  }
  .card-face {
    position: relative;
    width: 100%;
    height: 100%;
    border-radius: 28px;
    background: var(--card-black);
    overflow: hidden;
  }
  .family-tree-mark {
    position: absolute;
    left: 26px;
    top: 22px;
    width: 220px;
    height: 250px;
    border-radius: 48% 52% 12% 12% / 55% 55% 10% 10%;
    background: radial-gradient(ellipse at 50% 40%, var(--accent-red) 0%, var(--accent-red-dark) 75%, transparent 100%);
  }
  .family-tree-ghost {
    position: absolute;
    right: 20px;
    top: 200px;
    width: 215px;
    height: 290px;
    border-radius: 48% 52% 8% 8% / 45% 45% 6% 6%;
    background: radial-gradient(ellipse at 50% 40%, var(--ghost) 0%, #0c0c0c 80%, transparent 100%);
  }
  .role-tagline {
    position: absolute;
    left: 330px;
    top: 58px;
    font-family: "Dancing Script", cursive;
    font-size: 20px;
    color: var(--accent-red);
    white-space: nowrap;
  }
  .therapist-name {
    position: absolute;
    left: 272px;
    top: 88px;
    padding-right: 12px;
    font-family: "Parisienne", cursive;
    font-weight: 400;
    font-size: 60px;
    line-height: 1.2;
    white-space: nowrap;
    background: linear-gradient(180deg, var(--silver-light) 0%, var(--silver-mid) 55%, var(--silver-dark) 100%);
    -webkit-background-clip: text;
    background-clip: text;
    color: transparent;
  }
  .credentials {
    position: absolute;
    left: 278px;
    top: 176px;
    font-family: "Crimson Text", serif;
    font-size: 17px;
    color: var(--accent-red);
    white-space: nowrap;
  }
  .contact-list {
    position: absolute;
    left: 38px;
    bottom: 46px;
    list-style: none;
    font-family: "Open Sans", sans-serif;
    font-size: 26px;
    color: var(--contact-text);
  }
  .contact-item {
    display: flex;
    align-items: center;
    gap: 12px;
    line-height: 38px;
    white-space: nowrap;
  }
  .contact-icon {
    width: 22px;
    height: 22px;
    fill: var(--accent-red);
    flex-shrink: 0;
  }
</style>
</head>
<body>
<main class="canvas">
  <section class="business-card">
    <div class="card-frame">
      <div class="card-face">
        <div class="family-tree-ghost" role="img" aria-label="Faint decorative tree with family figures"></div>
        <div class="family-tree-mark" role="img" aria-label="Red tree illustration with parent and child figures"></div>

        <p class="role-tagline">In Home Therapist</p>
        <h1 class="therapist-name">Lena Brightwell</h1>
        <p class="credentials">MS, MFT Intern Marriage and Family Therapy</p>

        <ul class="contact-list">
          <li class="contact-item">
            <svg class="contact-icon" viewBox="0 0 24 24" aria-hidden="true">
              <path d="M6.6 10.8a15.1 15.1 0 0 0 6.6 6.6l2.2-2.2a1 1 0 0 1 1-.25 11.4 11.4 0 0 0 3.6.57 1 1 0 0 1 1 1V20a1 1 0 0 1-1 1A17 17 0 0 1 3 4a1 1 0 0 1 1-1h3.5a1 1 0 0 1 1 1c0 1.25.2 2.45.57 3.57a1 1 0 0 1-.25 1z"/>
            </svg>
            <span>617-482-5190</span>
          </li>
          <li class="contact-item">
            <svg class="contact-icon" viewBox="0 0 24 24" aria-hidden="true">
              <path d="M2 6h20v12H2z M2 6l10 7 10-7" fill="var(--accent-red)" stroke="#020202" stroke-width="1.4"/>
            </svg>
            <span>Lena@LenaBrightwell-example.com</span>
          </li>
        </ul>
      </div>
    </div>
  </section>
</main>
</body>
</html>
```